Business Card Design

We need a business card design for a new company. We produce and sell fully grown topiary (please Google topiary pictures if you are not familiar with Topiary).We make many different topiary designs and shapes in all sizes. Ranging from cute little table top animal sculptures such as bunnies and swans for the indoors, to big sculptures such as actual size elephants for outdoor gardens and parks. We also make topiary balls, spiral shapes and other attractive geometrical shapes for indoor and outdoor decorations. We want to see designs that reflects the playfulness and ,liveliness and cute characteristics of our products.Please find attached the logo.Thank you

Industry/Entity Type

Business

Contact Information for Business Card

Company Name : Leaf Forge
Slogan : Shaping Every Garden Bright
Tagline: Topiary...and more
Website : www.leafforge.example

Name on Card : Youssef Nabil Darwish
Title : Founder & CEO
email: youssef_nabil@leafforge.example

Address : 27 El-Masry Street
Ground Floor,Ste.1
El-Marg,Cairo,Egypt

Office Telephone : (02) 25948017
Mobile Number : 01287719462

Requirements
Must have
• The business card must have a white background.

```html
<!DOCTYPE html>
<html lang="en">
<head>
<meta charset="utf-8">
<title>Leaf Forge – Business Card</title>
<link rel="stylesheet" href="https://fonts.googleapis.com/css2?family=Arimo:wght@400;700&display=swap">
<style>
  :root {
    --leaf: #5b9a3a;
    --slate: #4b4b4d;
    --ink: #353535;
    --card: #ffffff;
    --backdrop: #ecebe6;
  }
  * { margin: 0; padding: 0; box-sizing: border-box; }
  html, body {
    width: 1200px; height: 834px; overflow: hidden;
    background: var(--backdrop);
    font-family: "Arimo", Arial, sans-serif;
  }
  .card {
    position: absolute; left: 20px; top: 23px;
    width: 1160px; height: 787px;
    background: var(--card);
    border-radius: 56px;
    overflow: hidden;
    box-shadow: 0 4px 18px rgba(0,0,0,.15);
    color: var(--ink);
  }
  .accent-bar {
    position: absolute; left: 0; top: 94px;
    width: 20px; height: 99px; background: var(--leaf);
  }
  .person { position: absolute; left: 70px; top: 98px; }
  .person-name {
    font-size: 36px; font-weight: 700; color: var(--leaf);
    text-transform: uppercase; letter-spacing: .5px; line-height: 1;
  }
  .person-title { font-size: 34px; margin-top: 12px; line-height: 1; }
  .address {
    position: absolute; left: 70px; top: 274px;
    font-size: 29px; line-height: 43px; font-style: normal;
  }
  .contacts { position: absolute; left: 70px; top: 482px; list-style: none; }
  .contacts li {
    display: flex; align-items: center; gap: 14px;
    font-size: 31px; height: 52px;
  }
  .contacts svg { width: 20px; height: 24px; flex: none; }
  .brand {
    position: absolute; left: 560px; top: 300px; width: 560px;
    text-align: center; color: var(--leaf);
  }
  .brand-name { font-size: 92px; font-weight: 400; line-height: 1; }
  .brand-slogan { font-size: 30px; margin-top: 18px; }
  .bands { position: absolute; left: 0; top: 0; width: 1160px; height: 787px; }
  .website {
    position: absolute; left: 70px; top: 680px;
    font-size: 30px; letter-spacing: 2px; color: #fff; line-height: 36px;
  }
  .tagline {
    position: absolute; left: 834px; top: 688px;
    font-size: 32px; color: #fff; line-height: 36px;
  }
</style>
</head>
<body>
  <section class="card">
    <svg class="bands" viewBox="0 0 1160 787" aria-hidden="true">
      <rect x="0" y="677" width="900" height="60" fill="var(--leaf)"/>
      <path d="M1160 677 L830 677 C790 677 790 719 750 719 L0 719 L0 787 L1160 787 Z" fill="var(--slate)"/>
    </svg>

    <div class="accent-bar"></div>
    <header class="person">
      <h1 class="person-name">Youssef Nabil Darwish</h1>
      <p class="person-title">Founder &amp; CEO</p>
    </header>

    <address class="address">
      27 El-Masry Street Ground<br>
      Floor,Ste.1<br>
      El-Marg,Cairo,Egypt
    </address>

    <ul class="contacts">
      <li>
        <svg viewBox="0 0 20 24"><rect x="4" y="1" width="12" height="22" rx="2" fill="var(--leaf)"/><rect x="6" y="4" width="8" height="11" fill="#fff"/><circle cx="10" cy="19" r="1.6" fill="#fff"/></svg>
        01287719462
      </li>
      <li>
        <svg viewBox="0 0 20 24"><path d="M5 4c2 0 3 4 2 5l-1 1c1 3 3 5 5 6l1-1c1-1 5 0 5 2l-1 3c-8 0-14-7-14-14z" fill="none" stroke="var(--leaf)" stroke-width="2"/></svg>
        (02) 25948017
      </li>
      <li>
        <svg viewBox="0 0 20 24"><rect x="1" y="7" width="18" height="12" rx="1" fill="var(--leaf)"/><path d="M2 8l8 6 8-6" fill="none" stroke="#fff" stroke-width="1.6"/></svg>
        youssef_nabil@leafforge.example
      </li>
    </ul>

    <div class="brand">
      <p class="brand-name">Leaf Forge</p>
      <p class="brand-slogan">Shaping Every Garden Bright</p>
    </div>

    <p class="website">www.leafforge.example</p>
    <p class="tagline">Topiary...and more</p>
  </section>
</body>
</html>
```